Business Card Design

Non-profit organization creating opportunities for:
Personal empowerment
Community Outreach
Healthier Life Choices
Body/Mind/Spirit Nourishment
Emotional Transformation
Charity & Network Opportunities
Everyday people making An extrodinary sufferance
All achieved from the Source within YOU.
Organization logo is the ying yang symbol with a small circle above it as if it were the head and the ying yang symbol was the body.  Also in side upper ying needs to be a heart and in the lower yang needs to be the letter C. This is very important as it came to me in a dream n the forming of this organization.  Color choice is open although a thought I hade was that the heart is red metallic foil (sine a red heart is the symbol of love)and the c is gold foil( the gifts of the 3 wise men and gold being one of them).a verticle card is preferred and logo as large as possible on it even if ying yang is made oval Ilook forward to the layouts and designs you can come up with.

Contact Information for Business Card
Lumen Harbor. Org
Paul Marsky
Executive Director
Lumen harbor.paul@brindlemail.com
512-394-2086

```html
<!DOCTYPE html>
<html lang="en">
<head>
<meta charset="utf-8">
<title>Lumen Harbor.Org – Business Card</title>
<link rel="stylesheet" href="https://fonts.googleapis.com/css2?family=Questrial&display=swap">
<style>
  :root {
    --backdrop: #2a2626;
    --card-black: #0b0b0c;
    --card-charcoal: #1c1c1f;
    --gold: #c9a448;
    --gold-light: #e6c876;
    --red: #d9202a;
    --cream: #e8dcc0;
  }
  * { box-sizing: border-box; margin: 0; padding: 0; }
  html, body {
    width: 1200px;
    height: 1040px;
    overflow: hidden;
    background: var(--backdrop);
  }
  .canvas {
    position: relative;
    width: 1200px;
    height: 1040px;
    display: flex;
    justify-content: center;
    align-items: center;
    gap: 40px;
  }
  .card {
    width: 480px;
    height: 840px;
    border-radius: 6px;
    position: relative;
    overflow: hidden;
  }

  /* Front */
  .card-front {
    background: var(--card-black);
    padding: 22px;
  }
  .front-frame {
    width: 100%;
    height: 100%;
    border: 5px solid var(--gold);
    box-shadow: inset 0 0 0 2px var(--gold-light);
    display: flex;
    flex-direction: column;
    align-items: center;
    justify-content: center;
    gap: 56px;
  }
  .front-mark {
    width: 300px;
    height: 300px;
    border-radius: 50%;
    background: var(--red);
  }
  .org-name {
    font-family: "Questrial", sans-serif;
    font-weight: 400;
    color: var(--red);
    font-size: 46px;
    line-height: 1.2;
    text-align: center;
  }

  /* Back */
  .card-back {
    background: radial-gradient(ellipse at 50% 55%, var(--card-charcoal) 0%, var(--card-black) 75%);
    font-family: "Questrial", sans-serif;
    text-align: center;
    padding: 40px 30px;
  }
  .contact-name {
    color: var(--red);
    font-size: 24px;
    letter-spacing: 0.5px;
  }
  .contact-title {
    color: var(--cream);
    font-size: 13px;
    margin-top: 8px;
  }
  .contact-phone {
    color: var(--gold-light);
    font-size: 22px;
    margin-top: 40px;
  }
  .contact-email {
    color: var(--gold-light);
    font-size: 16px;
    margin-top: 8px;
  }
  .mission {
    list-style: none;
    margin-top: 80px;
    font-size: 21px;
    line-height: 1.3;
  }
  .mission .gold { color: var(--gold); }
  .mission .red { color: var(--red); }
</style>
</head>
<body>
  <main class="canvas">
    <section class="card card-front" aria-label="Card front">
      <div class="front-frame">
        <div class="front-mark" aria-hidden="true"></div>
        <p class="org-name">Lumen<br>Harbor.Org</p>
      </div>
    </section>

    <section class="card card-back" aria-label="Card back">
      <p class="contact-name">Paul Marsky</p>
      <p class="contact-title">Executive Director</p>
      <p class="contact-phone">512-394-2086</p>
      <p class="contact-email">Lumen harbor.paul@brindlemail.com</p>
      <ul class="mission">
        <li class="gold">Personal empowerment</li>
        <li class="red">Community Outreach</li>
        <li class="gold">Healthier Life Choices</li>
        <li class="red">Body/Mind/Spirit</li>
        <li class="gold">Nourishment</li>
        <li class="gold">Emotional Transformation</li>
        <li class="red">Charity &amp;</li>
        <li class="red">Network Opportunities</li>
        <li class="gold">Everyday people making An</li>
        <li class="gold">extrodinary sufferance</li>
        <li class="red">All achieved from the Source</li>
        <li class="red">within YOU.</li>
      </ul>
    </section>
  </main>
</body>
</html>
```